Re-branding for Structural Engineering firm

We need new business cards as part of our current re-branding. We have a new logo (attached), so the card design should incorporate this color scheme. We are a structural engineering firm providing structural building design and seismic consulting services. The final design should communicate professionalism and stability, with a modern look and feel.

```html
<!DOCTYPE html>
<html lang="en">
<head>
<meta charset="utf-8">
<title>Alden Structural – Business Card</title>
<link rel="stylesheet" href="https://fonts.googleapis.com/css2?family=Lato:wght@400;700&family=Roboto:wght@400;500;700&display=swap">
<style>
  :root {
    --brand-blue: #1d72b8;
    --brand-blue-deep: #1a69ad;
    --brand-grey: #7d7e80;
    --ink: #2a2a2a;
    --rule: #6f6f6f;
    --paper: #ffffff;
    --paper-shade: #e9e9ea;
    --backdrop: #e4e2de;
  }
  * { box-sizing: border-box; margin: 0; padding: 0; }
  html, body { width: 900px; height: 1200px; overflow: hidden; }
  body { background: var(--backdrop); position: relative; font-family: "Lato", sans-serif; }

  .card {
    position: absolute;
    left: 86px;
    width: 727px;
    height: 425px;
    box-shadow: 0 4px 14px rgba(0,0,0,0.25);
    overflow: hidden;
  }
  .card--front {
    top: 130px;
    background: linear-gradient(to bottom, var(--paper) 0%, var(--paper) 55%, var(--paper-shade) 100%);
  }
  .card--back {
    top: 641px;
    background: linear-gradient(to bottom, #1f76bd 0%, var(--brand-blue-deep) 100%);
  }

  /* front: brand block */
  .brand-mark {
    position: absolute; left: 47px; top: 56px;
    width: 142px; height: 142px;
    background: var(--brand-blue);
  }
  .brand-divider {
    position: absolute; left: 199px; top: 56px;
    width: 3px; height: 142px;
    background: var(--brand-blue);
  }
  .brand-name {
    position: absolute; left: 208px; top: 52px;
    font-family: "Lato", sans-serif; font-weight: 700;
    font-size: 37px; line-height: 38px;
    color: var(--brand-blue);
    letter-spacing: 0.2px;
  }
  .firm-address {
    position: absolute; left: 208px; top: 134px;
    font-size: 18.5px; line-height: 23px;
    color: var(--brand-grey);
  }
  .firm-address .sep { color: var(--brand-blue); padding: 0 8px; }

  .contact-rule {
    position: absolute; left: 47px; top: 319px;
    width: 632px; height: 2px;
    background: var(--rule);
  }
  .person {
    position: absolute; left: 47px; top: 335px;
    font-family: "Roboto", sans-serif;
  }
  .person__name { font-weight: 700; font-size: 19px; color: var(--ink); letter-spacing: 0.3px; }
  .person__role { font-size: 16px; color: var(--brand-blue); margin-top: 4px; }

  .direct-contact {
    position: absolute; right: 48px; top: 335px;
    font-family: "Roboto", sans-serif; font-size: 15.5px; color: var(--ink);
    text-align: right; line-height: 22px;
  }
  .direct-contact__line { display: flex; align-items: center; justify-content: flex-end; gap: 7px; }
  .direct-contact svg { display: block; }

  .accent-band { position: absolute; left: 0; bottom: 0; width: 727px; height: 17px; }

  /* back */
  .back-mark {
    position: absolute; left: 56px; top: 209px;
    width: 132px; height: 132px;
    background: var(--paper);
  }
  .back-name {
    position: absolute; left: 56px; top: 342px;
    font-family: "Lato", sans-serif; font-weight: 700;
    font-size: 19px; line-height: 20px;
    color: var(--paper);
  }
</style>
</head>
<body>

  <section class="card card--front" aria-label="Business card front">
    <div class="brand-mark"></div>
    <div class="brand-divider"></div>
    <div class="brand-name">ALDEN<br>STRUCTURAL</div>
    <div class="firm-address">
      4410 Harbor Ridge Dr., Ste. 210<br>
      Carlsbad, California 92008<br>
      858.555.0142<span class="sep">|</span>www.aldense.com
    </div>

    <div class="contact-rule"></div>

    <div class="person">
      <div class="person__name">DANA WHITFIELD, S.E.</div>
      <div class="person__role">Principal</div>
    </div>

    <div class="direct-contact">
      <div class="direct-contact__line">619.555.0187
        <svg width="11" height="15" viewBox="0 0 11 15" aria-hidden="true">
          <rect x="0.8" y="0.8" width="9.4" height="13.4" rx="1.6" fill="none" stroke="#1d72b8" stroke-width="1.6"/>
          <rect x="2.6" y="2.8" width="5.8" height="8" fill="#1d72b8"/>
        </svg>
      </div>
      <div class="direct-contact__line">dana@aldense.com
        <svg width="15" height="11" viewBox="0 0 15 11" aria-hidden="true">
          <rect x="0" y="0" width="15" height="11" fill="#1d72b8"/>
          <path d="M0.8 0.8 L7.5 6 L14.2 0.8" fill="none" stroke="#fff" stroke-width="1.2"/>
        </svg>
      </div>
    </div>

    <svg class="accent-band" viewBox="0 0 727 17" preserveAspectRatio="none" aria-hidden="true">
      <polygon points="0,0 362,0 370,17 0,17" fill="#1d72b8"/>
      <polygon points="362,0 727,0 727,17 370,17" fill="#8a8b8d"/>
    </svg>
  </section>

  <section class="card card--back" aria-label="Business card back">
    <div class="back-mark"></div>
    <div class="back-name">ALDEN<br>STRUCTURAL</div>
  </section>

</body>
</html>
```